Retractable Banner Design for Retail Shopping Event

I need a design for a 33” by 86” retractable banner. It should have my logo at the top (the largest element of the design) and the banner should also include my website and Instagram handle:
www.verikamode.com
@verikamode
I have included product pictures in the brief that can be used. I also included different versions of my logo file, including AI. I need the file to be ready to upload to my printer.
My store is an upscale women’s boutique. I am also attaching designs I have selected in the past to give an idea of my aesthetic.

```html
<!DOCTYPE html>
<html lang="en">
<head>
<meta charset="utf-8">
<title>Verika Mode – Retractable Banner</title>
<link rel="stylesheet" href="https://fonts.googleapis.com/css2?family=Poppins:wght@400&display=swap">
<style>
  :root {
    --backdrop: #8b8b8b;
    --blush-light: #f3e3df;
    --blush: #ecd3ce;
    --rose-band: #c9aea7;
    --ring: #ebd5cf;
    --panel-top: #ffffff;
    --panel-bottom: #e2e2e2;
    --name-grey: #6f6f6f;
    --ink: #262626;
  }
  * { box-sizing: border-box; margin: 0; padding: 0; }
  html, body {
    width: 1200px;
    height: 900px;
    overflow: hidden;
    background: var(--backdrop);
  }
  .banner {
    position: absolute;
    left: 450px;
    top: 20px;
    width: 300px;
    height: 860px;
    display: flex;
    flex-direction: column;
    background: var(--panel-top);
  }
  .banner__header {
    height: 220px;
    background: linear-gradient(180deg, var(--blush-light), var(--blush));
    display: flex;
    align-items: center;
    justify-content: center;
  }
  .brand-name {
    font-family: "Poppins", sans-serif;
    font-weight: 400;
    font-size: 30px;
    letter-spacing: 3px;
    color: var(--name-grey);
    white-space: nowrap;
  }
  .banner__products {
    flex: 1;
    background: linear-gradient(180deg, var(--panel-top), var(--panel-bottom));
    display: grid;
    grid-template-columns: repeat(2, 124px);
    grid-template-rows: repeat(3, 1fr);
    justify-content: space-evenly;
    align-items: center;
    padding: 16px 0 20px;
  }
  .product {
    width: 124px;
    height: 124px;
    border-radius: 50%;
    border: 3px solid var(--ring);
    overflow: hidden;
    background: #ffffff;
    box-shadow: 0 14px 10px -10px rgba(0, 0, 0, 0.22);
  }
  .product__image { width: 100%; height: 100%; }
  .product__image--earrings { background: linear-gradient(135deg, #ffffff 15%, #ead9a4 50%, #ffffff 85%); }
  .product__image--slippers { background: linear-gradient(160deg, #f6f3f4 10%, #e9d6d0 45%, #b7a4ae 75%, #f4f1f2 95%); }
  .product__image--tray { background: linear-gradient(170deg, #f5f3f0 12%, #c8a873 40%, #7a6650 65%, #f2efeb 90%); }
  .product__image--tote { background: linear-gradient(180deg, #f1e8ec 10%, #d4bcae 35%, #cbb2a3 75%, #efe6ea 95%); }
  .product__image--sweater { background: linear-gradient(180deg, #ecebe9 10%, #c4c4c2 45%, #b9b9b7 75%, #efefed 95%); }
  .product__image--headband { background: linear-gradient(140deg, #f3f3f2 12%, #b3b5b2 45%, #7f817e 65%, #f2f2f1 90%); }
  .banner__footer {
    height: 110px;
    background: var(--rose-band);
    display: flex;
    flex-direction: column;
    align-items: center;
    justify-content: center;
    gap: 2px;
    font-family: "Poppins", sans-serif;
    font-weight: 400;
    font-size: 18px;
    line-height: 1.35;
    color: var(--ink);
  }
</style>
</head>
<body>
  <main class="banner">
    <header class="banner__header">
      <p class="brand-name">VERIKA MODE</p>
    </header>

    <section class="banner__products">
      <div class="product"><div class="product__image product__image--earrings" role="img" aria-label="Gold beaded clover stud earrings with crystal centres"></div></div>
      <div class="product"><div class="product__image product__image--slippers" role="img" aria-label="Blush pom-pom slide slippers"></div></div>
      <div class="product"><div class="product__image product__image--tray" role="img" aria-label="Round leopard print lacquer tray"></div></div>
      <div class="product"><div class="product__image product__image--tote" role="img" aria-label="Taupe tote bag with teal snake print"></div></div>
      <div class="product"><div class="product__image product__image--sweater" role="img" aria-label="Grey star sweater worn by a model"></div></div>
      <div class="product"><div class="product__image product__image--headband" role="img" aria-label="Grey knotted headband with gold star studs"></div></div>
    </section>

    <footer class="banner__footer">
      <p class="contact contact--web">www.verikamode.com</p>
      <p class="contact contact--social">@verikamode</p>
    </footer>
  </main>
</body>
</html>
```